Interior Design business card design

I am an interior decorator - dont want to specify decorating more just design.
Want organic looking logo - charcoal and white - with touch of lime green.
Like the idea of some sort of spiral in corner but writing in a line
want lower case, carlamintowe as one and designs in different font underneath. Maybe using c and m as logo.
More modern than traditional. My clients are mid to top end residential

Target Market(s)

medium to top end homeowners

Industry/Entity Type

Residential

Contact Information for Business Card

Carla Mintowe Designs
58 Fallowmere ave
Tindarra 2188 NSW
Tel 0417869214
carlamintowe@quellnet.com.au

Logo Text

Carla Mintowe Designs

Logo styles of interest
Abstract Logo
Lettermark Logo
Requirements
Must have
• Name address ph and e mail
Nice to have
• Contemporary
smart but organic
Should not have
• no traditional fonts

```html
<!DOCTYPE html>
<html lang="en">
<head>
<meta charset="utf-8">
<title>Carla Mintowe Designs – Business Card</title>
<link rel="stylesheet" href="https://fonts.googleapis.com/css2?family=Raleway:wght@200;300&family=Work+Sans:wght@300;400&display=swap">
<style>
  :root {
    --backdrop: #c9c9c9;
    --charcoal: #58585a;
    --ink: #1e1e1e;
    --paper: #ffffff;
    --lime: #8cc63f;
    --soft-white: #e4e4e4;
  }
  * { box-sizing: border-box; margin: 0; padding: 0; }
  html, body {
    width: 1200px;
    height: 900px;
    overflow: hidden;
    background: var(--backdrop);
  }
  .canvas {
    position: relative;
    width: 1200px;
    height: 900px;
  }
  .card {
    position: absolute;
    top: 300px;
    width: 525px;
    height: 300px;
    overflow: hidden;
  }

  /* Front */
  .card-front {
    left: 50px;
    background: var(--charcoal);
  }
  .front-name {
    position: absolute;
    left: 78px;
    top: 104px;
    font-family: "Raleway", sans-serif;
    font-weight: 200;
    font-size: 50px;
    letter-spacing: 0.5px;
    color: var(--paper);
    line-height: 1;
  }
  .front-rule {
    position: absolute;
    left: 148px;
    top: 172px;
    width: 142px;
    height: 4px;
    background: var(--lime);
  }
  .front-tagline {
    position: absolute;
    left: 102px;
    top: 186px;
    font-family: "Raleway", sans-serif;
    font-weight: 200;
    font-size: 21px;
    color: var(--soft-white);
    line-height: 1;
  }

  /* Back */
  .card-back {
    left: 625px;
    background: var(--paper);
    font-family: "Work Sans", sans-serif;
    font-weight: 300;
    color: var(--ink);
  }
  .brand-block {
    position: absolute;
    left: 28px;
    top: 52px;
    display: flex;
    align-items: center;
    gap: 8px;
  }
  .brand-dot {
    width: 14px;
    height: 14px;
    border-radius: 50%;
    background: var(--lime);
  }
  .brand-name {
    font-family: "Raleway", sans-serif;
    font-weight: 300;
    font-size: 22px;
    color: var(--charcoal);
  }
  .studio-name {
    position: absolute;
    left: 200px;
    top: 26px;
    font-size: 21px;
    letter-spacing: 0.5px;
  }
  .street-line {
    position: absolute;
    left: 196px;
    top: 56px;
    font-size: 36px;
    letter-spacing: 0.5px;
    line-height: 1;
  }
  .suburb-line {
    position: absolute;
    left: 200px;
    top: 106px;
    font-size: 18px;
    letter-spacing: 0.5px;
    line-height: 1;
  }
  .postcode {
    position: absolute;
    left: 400px;
    top: 96px;
    font-size: 40px;
    line-height: 1;
  }
  .phone-line {
    position: absolute;
    left: 200px;
    top: 128px;
    font-size: 16px;
    letter-spacing: 0.5px;
  }
  .email-line {
    position: absolute;
    left: 200px;
    top: 150px;
    font-size: 15px;
    letter-spacing: 0.3px;
  }
</style>
</head>
<body>
  <main class="canvas">
    <section class="card card-front" aria-label="Business card front">
      <h1 class="front-name">carlamintowe</h1>
      <div class="front-rule"></div>
      <p class="front-tagline">interior design</p>
    </section>

    <section class="card card-back" aria-label="Business card back">
      <div class="brand-block">
        <span class="brand-dot"></span>
        <span class="brand-name">carlamintowe</span>
      </div>
      <p class="studio-name">Carla Mintowe Designs</p>
      <p class="street-line">58 Fallowmere</p>
      <p class="suburb-line">ave Tindarra</p>
      <p class="postcode">2188</p>
      <p class="phone-line">NSW Tel 0417869214</p>
      <p class="email-line">carlamintowe@quellnet.com.au</p>
    </section>
  </main>
</body>
</html>
```